Brand new redesign of Brightwell finance website

I need a new website design that i can advertise a great low interest rate on the front page and capture input application details that will send through to my email address.

some car finance companies will be similar to this would be listed below

tallyfunds.com.au
corelinefinance.com.au
finance715.com.au
wexburyfinance.com.au
finance93.com.au

Reason: I have changed the project to a committed project. all the webpages should have the same format just different content and i want to be able to edit the front page easily to update my interest rates.

Reason: Provide more time for resubmission and submission work

Target Market(s)

Australian Finance market targeting a younger demographic

Industry/Entity Type

Finance

Coding

Coded - Design and coding required

Number of Pages Required

5+ page

Font styles to use
Serif
Sans Serif

Colors
0255a3
ffffff
cedeed

Requirements
Must have
• application capture form
• apply now buttons
• Headline rate front page

```html
<!DOCTYPE html>
<html lang="en">
<head>
<meta charset="utf-8">
<title>Brightwell Finance</title>
<link rel="stylesheet" href="https://fonts.googleapis.com/css2?family=Raleway:wght@400;500;600&family=Open+Sans:ital,wght@0,400;0,600;1,400&display=swap">
<style>
:root{
  --navy:#0255a3;
  --navy-deep:#073e8c;
  --nav-text:#1c4a8f;
  --sky:#1e90e3;
  --sky-light:#29a6f7;
  --ice:#cedeed;
  --white:#ffffff;
  --ink:#1d1d1d;
  --grey:#6b6b6b;
  --pale:#f0f0f0;
  --accent:#2b8fd6;
}
*{box-sizing:border-box;margin:0;padding:0}
html,body{width:1200px;height:2302px;overflow:hidden}
body{position:relative;background:var(--white);font-family:"Open Sans",Arial,sans-serif;color:var(--ink)}
.abs{position:absolute}

/* header */
.site-header{left:0;top:0;width:1200px;height:110px;background:var(--white)}
.brand{left:120px;top:31px;display:flex;align-items:center;gap:10px}
.brand-dot{width:46px;height:46px;border-radius:50%;background:var(--navy)}
.brand-name{font-family:"Raleway",sans-serif;font-weight:600;font-size:22px;color:var(--navy);letter-spacing:.3px}
.main-nav a{position:absolute;top:48px;font-family:"Raleway",sans-serif;font-size:15px;font-weight:500;color:var(--nav-text);text-decoration:none;letter-spacing:.3px}

/* hero */
.hero{left:0;top:110px;width:1200px;height:462px;background:linear-gradient(100deg,#2b5fae 0%,#3d7ac6 45%,#2a62b0 100%)}
.hero-kicker{left:118px;top:240px;font-family:"Raleway",sans-serif;font-size:30px;color:var(--white);font-weight:500}
.hero-title{left:118px;top:280px;font-family:"Raleway",sans-serif;font-size:40px;color:var(--white);font-weight:500}
.hero-points{left:120px;top:338px;list-style:none;color:var(--white);font-size:15px}
.hero-points li{height:37px;display:flex;align-items:center;gap:10px}
.hero-points li::before{content:"";border-left:6px solid var(--white);border-top:5px solid transparent;border-bottom:5px solid transparent}
.apply-form{left:764px;top:184px;width:312px;height:328px;background:#5aa6e8}
.apply-form h2{position:absolute;left:37px;top:17px;font-family:"Raleway",sans-serif;font-weight:400;font-size:26px;color:var(--white)}
.field{position:absolute;left:31px;width:251px;height:31px;background:linear-gradient(#ffffff,#ececec);border:1px solid #d5d5d5;font-size:11px;color:#8a8a8a;padding:8px 14px}
.field.message{height:76px}
.send-btn{position:absolute;left:31px;top:263px;width:251px;height:39px;background:var(--navy-deep);color:var(--white);font-family:"Raleway",sans-serif;font-size:21px;display:flex;align-items:center;justify-content:center}
.dot{width:18px;height:18px;border-radius:50%;background:var(--white);top:540px}
.dot.active{background:transparent;border:2px solid var(--white)}

/* welcome */
.welcome-title{left:123px;top:640px;font-family:"Raleway",sans-serif;font-size:28px;font-weight:400;color:#111;white-space:nowrap}
.welcome-title span{color:var(--accent)}
.welcome-lead{left:124px;top:694px;width:480px;font-size:14.5px;line-height:24px;color:#333}
.welcome-body{left:124px;top:751px;width:480px;font-size:13px;line-height:25px;color:var(--grey)}
.learn-btn{left:124px;top:849px;width:118px;height:33px;background:linear-gradient(#45aaf0,#1f86d6);color:var(--white);font-size:13px;font-weight:600;display:flex;align-items:center;justify-content:center}
.video{left:686px;top:637px;width:390px;height:250px;background:linear-gradient(120deg,#c9d3dc,#7d8a96 55%,#3b4148);overflow:hidden}
.video-play{position:absolute;left:159px;top:84px}
.video-bar{position:absolute;left:0;bottom:0;width:390px;height:29px;background:#2c2c2c}

/* cta band */
.cta-band{left:0;top:970px;width:1200px;height:265px;background:linear-gradient(90deg,#3e3e3e,#6c6c6c 50%,#4a4a4a)}
.cta-title{left:0;top:1038px;width:1200px;text-align:center;font-family:"Raleway",sans-serif;font-size:31px;font-weight:600;color:var(--white)}
.cta-sub{left:0;top:1087px;width:1200px;text-align:center;font-family:"Raleway",sans-serif;font-size:22px;font-weight:600;color:var(--white)}
.outline-btn{left:523px;top:1136px;width:149px;height:42px;border:2px solid var(--white);color:var(--white);font-size:15px;display:flex;align-items:center;justify-content:center}

/* services */
.service{top:1292px;width:234px;height:272px}
.service-img{height:146px}
.service-body{height:126px;text-align:center;padding-top:12px}
.service.dark .service-body{background:#0a4a9c;color:var(--white)}
.service.light .service-body{background:var(--ice);color:var(--navy)}
.service h3{font-family:"Raleway",sans-serif;font-weight:500;font-size:20px}
.service p{font-size:10.5px;line-height:15px;margin:6px 18px 0;opacity:.75}
.service .more{margin-top:12px;font-size:12px;font-weight:600;display:flex;align-items:center;justify-content:center;gap:6px}
.service.light .more{color:#111}
.arrow-circle{width:18px;height:18px;border-radius:50%;display:inline-flex;align-items:center;justify-content:center;background:var(--white)}

/* testimonial */
.testimonials{left:0;top:1631px;width:1200px;height:344px;background:var(--pale)}
.portrait{left:187px;top:1710px;width:202px;height:202px;border-radius:50%;border:4px solid #e2e2e2;background:linear-gradient(#e9e4df,#4f86d6)}
.testi-title{left:465px;top:1690px;font-family:"Raleway",sans-serif;font-size:27px;font-weight:400;color:#444}
.quote{left:453px;top:1752px;width:520px;font-style:italic;font-size:15.5px;line-height:33px;color:#777}
.quote-mark{font-family:Georgia,serif;font-size:60px;color:#999;line-height:1;font-style:normal}
.author{left:430px;top:1864px;font-size:15.5px;line-height:29px;color:#333}

/* footer */
.site-footer{left:0;top:1975px;width:1200px;height:255px;background:var(--sky)}
.footer-brand{left:150px;top:2040px;width:160px;text-align:center;color:var(--white)}
.footer-ring{width:70px;height:70px;border-radius:50%;border:3px solid var(--white);margin:0 auto 14px}
.footer-name{font-family:"Raleway",sans-serif;font-weight:600;font-size:22px;line-height:24px;letter-spacing:1px}
.footer-col{top:2027px;color:var(--white)}
.footer-col h4{font-family:"Raleway",sans-serif;font-weight:600;font-size:14.5px;margin-bottom:10px}
.footer-col li{list-style:none;font-size:13px;line-height:29px;padding-left:3px}
.footer-col p{font-size:13px;line-height:21px;padding-left:3px}
.legal{left:0;top:2230px;width:1200px;height:72px;background:var(--sky-light)}
.legal p{position:absolute;left:133px;top:20px;font-size:12px;color:var(--white)}
</style>
</head>
<body>

<header class="abs site-header">
  <div class="abs brand"><span class="brand-dot"></span><span class="brand-name">BRIGHTWELL FINANCE</span></div>
  <nav class="main-nav">
    <a style="left:509px">ABOUT</a>
    <a style="left:597px">SERVICES</a>
    <a style="left:703px">FINANCE</a>
    <a style="left:806px">APPLY NOW</a>
    <a style="left:928px">BLOG</a>
    <a style="left:1005px">CONTACT</a>
  </nav>
</header>

<section class="abs hero" role="img" aria-label="Blue-toned photo of an older couple reviewing paperwork with an adviser"></section>
<div class="abs hero-kicker">LOW RATE CAR FINANCE</div>
<h1 class="abs hero-title">RATES FROM 5.49% P.A.</h1>
<ul class="abs hero-points">
  <li>Cum sociis natoque penatibus</li>
  <li>Magnis dis parturient montes nascetur ridicu</li>
  <li>Duis quam Nam eget</li>
</ul>
<form class="abs apply-form">
  <h2>Let's Start Now</h2>
  <div class="field" style="top:63px">Full Name</div>
  <div class="field" style="top:101px">Email</div>
  <div class="field" style="top:138px">Phone</div>
  <div class="field message" style="top:177px">Message</div>
  <div class="send-btn">Send</div>
</form>
<span class="abs dot active" style="left:563px"></span>
<span class="abs dot" style="left:586px"></span>
<span class="abs dot" style="left:608px"></span>
<span class="abs dot" style="left:629px"></span>

<h2 class="abs welcome-title">WELCOME TO <span>BRIGHTWELL FINANCE</span></h2>
<p class="abs welcome-lead">At justo id velit placerat molestie Donec dictum lectus non odio Cras a ante vitae enim iaculis aliquam Mauris</p>
<p class="abs welcome-body">venenatis nec euismod sit amet egestas placerat est Pellentesque habitant morbi tristique senectus et netus et malesuada fames ac turpis egestas Cras id elit Integer quis urna Ut ante enim dapibus malesuada</p>
<div class="abs learn-btn">Learn More</div>
<div class="abs video" role="img" aria-label="Video still of two businessmen talking in an office">
  <svg class="video-play" width="52" height="52" viewBox="0 0 52 52"><circle cx="26" cy="26" r="25" fill="#fff"/><path d="M20 15 L37 26 L20 37 Z" fill="#111"/></svg>
  <div class="video-bar">
    <svg width="390" height="29" viewBox="0 0 390 29">
      <path d="M10 9 L18 14.5 L10 20 Z" fill="#fff"/>
      <rect x="30" y="12" width="295" height="5" rx="2.5" fill="#ddd"/>
      <rect x="30" y="12" width="105" height="5" rx="2.5" fill="#3a8ee6"/>
      <path d="M357 11 h4 l5 -4 v15 l-5 -4 h-4 Z" fill="#fff"/>
      <path d="M369 10 q4 4.5 0 9" stroke="#fff" stroke-width="1.5" fill="none"/>
    </svg>
  </div>
</div>

<section class="abs cta-band" role="img" aria-label="Darkened photo of a smiling woman meeting a client at a desk"></section>
<h2 class="abs cta-title">CUM SOCIIS NATOQUE PENATIBUS ET MAGNIS</h2>
<p class="abs cta-sub">DIS PARTURIENT MONTES NASCETUR RIDICU</p>
<div class="abs outline-btn">APPLY NOW</div>

<article class="abs service dark" style="left:124px">
  <div class="service-img" role="img" aria-label="Photo of a couple meeting an adviser in an office" style="background:linear-gradient(#e8ecef,#b9c3cc)"></div>
  <div class="service-body"><h3>Bas Agent</h3><p>Cum sociis natoque penatibus et magnis dis parturient montes nascetu</p>
  <div class="more">Learn More <span class="arrow-circle"><svg width="8" height="10" viewBox="0 0 8 10"><path d="M2 1 L6 5 L2 9" stroke="#0a4a9c" stroke-width="2" fill="none"/></svg></span></div></div>
</article>
<article class="abs service light" style="left:370px">
  <div class="service-img" role="img" aria-label="Photo of a blue payroll binder with a calculator" style="background:linear-gradient(#b6c9e6,#3f6fbf)"></div>
  <div class="service-body"><h3>Payroll &amp; Bookeeping</h3><p>Cum sociis natoque penatibus et magnis dis parturient montes nascetu</p>
  <div class="more">Learn More <span class="arrow-circle"><svg width="8" height="10" viewBox="0 0 8 10"><path d="M2 1 L6 5 L2 9" stroke="#111" stroke-width="2" fill="none"/></svg></span></div></div>
</article>
<article class="abs service dark" style="left:614px">
  <div class="service-img" role="img" aria-label="Photo of hands reviewing documents beside a laptop" style="background:linear-gradient(#d9dcdf,#8e949b)"></div>
  <div class="service-body"><h3>Credit File Repair</h3><p>Cum sociis natoque penatibus et magnis dis parturient montes nascetu</p>
  <div class="more">Learn More <span class="arrow-circle"><svg width="8" height="10" viewBox="0 0 8 10"><path d="M2 1 L6 5 L2 9" stroke="#0a4a9c" stroke-width="2" fill="none"/></svg></span></div></div>
</article>
<article class="abs service light" style="left:858px">
  <div class="service-img" role="img" aria-label="Photo of a calculator, coins and a pen on paperwork" style="background:linear-gradient(#eef0f2,#c9b68a)"></div>
  <div class="service-body"><h3>Debt Consolidation</h3><p>Cum sociis natoque penatibus et magnis dis parturient montes nascetu</p>
  <div class="more">Learn More <span class="arrow-circle"><svg width="8" height="10" viewBox="0 0 8 10"><path d="M2 1 L6 5 L2 9" stroke="#111" stroke-width="2" fill="none"/></svg></span></div></div>
</article>

<section class="abs testimonials"></section>
<div class="abs portrait" role="img" aria-label="Portrait photo of a smiling customer in a blue top"></div>
<h2 class="abs testi-title">What Our People Says</h2>
<blockquote class="abs quote"><span class="quote-mark" style="position:absolute;left:-40px;top:-6px">&ldquo;</span>Maecenas aliquet velit vel turpis Mauris neque metus malesuada nec ultricies sit amet porttitor mattis enim In massa libero interdum nec interdum vel blandit sed nulla In ullamcorper est eget tempor cursus<span class="quote-mark" style="position:absolute;left:425px;top:70px">&rdquo;</span></blockquote>
<p class="abs author">By Author Name,<br>City Location</p>

<footer class="abs site-footer"></footer>
<div class="abs footer-brand"><div class="footer-ring"></div><div class="footer-name">BRIGHTWELL<br>FINANCE</div></div>
<div class="abs footer-col" style="left:344px"><h4>COMPANY</h4><ul><li>Home</li><li>Why We are</li><li>About Us</li><li>Our Team</li></ul></div>
<div class="abs footer-col" style="left:506px"><h4>RESOURCES</h4><ul><li>Help</li><li>FAQ</li><li>Sitemap</li><li>Term of Use</li></ul></div>
<div class="abs footer-col" style="left:671px"><h4>SUPPORT</h4><ul><li>Support</li><li>News &amp; Blogs</li><li>Cients</li><li>Contcat Us</li></ul></div>
<div class="abs footer-col" style="left:849px"><h4>CONTACT US</h4>
  <p style="margin-top:14px">Marlow Lane Offices Level 2<br>14 Surry Hills 2010</p>
  <p style="margin-top:10px">T 02 5550 1834</p>
  <p style="margin-top:10px">info@brightwellfinance.com.au</p>
</div>
<div class="abs legal"><p>&copy; 2016 Company Name &nbsp;All right reserved</p></div>

</body>
</html>
```